Brochure Design Project

Color brochure with text, graphics, and photos. (I will provide the text). 4 pages of 8 1/2 X 11". This is a brochure about dental implants.
Attached is the text and logo for the brochure.

See new parameters and information on the brochure project.

Included in the brochure is our address: Brookfield Dental Care, 218 Larchmont Avenue, Brookfield, PA 17342.  717-482-6915.  www.brookfielddentalcare-example.com.

Martin R. Pulaski, D.M.D., M.A.G.D., F.I.C.O.I. (Attached is photo for brochure)file://localhost/Users/mrpdmd7/Pictures/iPhoto%20Library/Masters/2003/Office%20Pictures/Dr.%20Pulaski%202.jpg

Target Market(s)

Adults, primarily senior adults.

Industry/Entity Type

Dental

```html
<!DOCTYPE html>
<html lang="en">
<head>
<meta charset="utf-8">
<title>Brookfield Dental Care – The Magic of Dental Implants</title>
<link rel="stylesheet" href="https://fonts.googleapis.com/css2?family=Open+Sans:wght@400;700&family=Tinos:wght@700&display=swap">
<style>
  :root {
    --page-bg: #e6e6e4;
    --paper: #ffffff;
    --brand-blue: #1b5fae;
    --navy: #173f7a;
    --orange: #f8ad55;
    --ink: #222222;
    --photo-grey-1: #d9d8d2;
    --photo-grey-2: #6b6d72;
    --photo-warm-1: #f1ddd0;
    --photo-warm-2: #c98f6e;
    --photo-green: #4cae4f;
    --tooth-1: #ffffff;
    --tooth-2: #c9ccd1;
  }
  * { margin: 0; padding: 0; box-sizing: border-box; }
  html, body { width: 1200px; height: 900px; overflow: hidden; }
  body { background: var(--page-bg); font-family: "Open Sans", Arial, sans-serif; position: relative; }

  .brochure-spread {
    position: absolute; left: 41px; top: 89px; width: 1117px; height: 721px;
    background: var(--paper); overflow: hidden;
    box-shadow: 0 2px 6px rgba(0,0,0,.25);
  }
  .top-band { position: absolute; left: 0; top: 0; width: 100%; height: 14px; background: var(--brand-blue); z-index: 3; }
  .fold-line { position: absolute; left: 558px; top: 0; height: 100%; border-left: 1px dashed #555; z-index: 4; }

  .cover-photo {
    position: absolute; left: 576px; top: 150px; width: 541px; height: 400px;
    background: linear-gradient(90deg, var(--photo-warm-1) 0%, var(--photo-warm-2) 35%, #f3efe9 55%, var(--photo-warm-2) 72%, var(--photo-green) 88%);
  }
  .wave-layer { position: absolute; left: 0; top: 0; width: 1117px; height: 721px; z-index: 1; }

  .back-panel { position: absolute; left: 0; top: 0; width: 558px; height: 100%; text-align: center; z-index: 2; }
  .doctor-photo {
    position: absolute; left: 210px; top: 41px; width: 152px; height: 195px;
    background: linear-gradient(180deg, var(--photo-grey-1) 0%, #b9b6ae 55%, var(--photo-grey-2) 100%);
  }
  .doctor-name { position: absolute; left: 0; width: 572px; top: 246px; font-weight: 700; font-size: 14px; color: var(--brand-blue); }
  .doctor-credentials { position: absolute; left: 0; width: 572px; top: 264px; font-size: 11px; color: var(--ink); }

  .brand-mark { display: flex; align-items: center; justify-content: center; gap: 8px; font-weight: 700; color: var(--navy); }
  .brand-dot { width: 16px; height: 16px; border-radius: 50%; background: var(--brand-blue); flex: none; }
  .back-brand { position: absolute; left: 0; width: 572px; top: 350px; font-size: 15px; }

  .practice-name { position: absolute; left: 0; width: 572px; top: 422px; font-weight: 700; font-size: 14px; color: var(--orange); }
  .practice-address { position: absolute; left: 0; width: 572px; top: 443px; font-size: 10px; color: var(--ink); line-height: 14px; }
  .practice-phone { position: absolute; left: 0; width: 572px; top: 481px; font-weight: 700; font-size: 14px; color: var(--orange); }

  .cover-panel { position: absolute; left: 559px; top: 0; width: 558px; height: 100%; z-index: 2; }
  .cover-brand { position: absolute; left: 0; width: 534px; top: 86px; font-size: 20px; }
  .cover-title {
    position: absolute; left: 51px; top: 580px;
    font-family: "Tinos", "Times New Roman", serif; font-weight: 700; font-size: 37px; line-height: 42px; color: #ffffff;
  }
  .tooth-figure {
    position: absolute; left: 362px; top: 510px; width: 170px; height: 190px; border-radius: 40px 40px 50px 50px;
    background: radial-gradient(circle at 40% 30%, var(--tooth-1) 0%, #eceef1 45%, var(--tooth-2) 100%);
  }
</style>
</head>
<body>
  <main class="brochure-spread">
    <div class="top-band"></div>

    <div class="cover-photo" role="img" aria-label="Photo of three smiling adult patients, a young woman, an older woman and an older man"></div>

    <svg class="wave-layer" viewBox="0 0 1117 721" aria-hidden="true">
      <path d="M0,425 C130,515 340,545 560,535 C760,520 900,465 1117,462 L1117,721 L0,721 Z" fill="var(--orange)"/>
      <path d="M0,548 C150,600 380,590 560,548 C760,505 900,475 1117,478 L1117,721 L0,721 Z" fill="var(--paper)"/>
      <path d="M0,598 C170,630 400,610 560,540 C730,480 900,470 1117,484 L1117,721 L0,721 Z" fill="var(--brand-blue)"/>
    </svg>

    <div class="fold-line"></div>

    <section class="back-panel">
      <div class="doctor-photo" role="img" aria-label="Portrait photo of Dr. Pulaski in a dark suit"></div>
      <p class="doctor-name">Dr. Martin R. Pulaski</p>
      <p class="doctor-credentials">D.M.D., M.A.G.D., F.I.C.O.I.</p>

      <div class="brand-mark back-brand"><span class="brand-dot"></span>Brookfield Dental Care</div>

      <p class="practice-name">Brookfield Dental Care</p>
      <p class="practice-address">218 Larchmont Avenue, Brookfield, PA 17342<br>www.brookfielddentalcare-example.com</p>
      <p class="practice-phone">Call us: 717-482-6915</p>
    </section>

    <section class="cover-panel">
      <div class="brand-mark cover-brand"><span class="brand-dot"></span>Brookfield Dental Care</div>
      <h1 class="cover-title">The Magic of<br>Dental implants</h1>
      <div class="tooth-figure" role="img" aria-label="Illustration of a cartoon tooth character holding a magic wand"></div>
    </section>
  </main>
</body>
</html>
```